BSC Flyer to attract applicants 11x17

Brightline Stagecraft Company provides crew for local concerts, filming, theater, and corporate events.
The flyer will be posted on bulletin boards at colleges with theater programs.
Our primary venues are historic theaters in downtown LA
Need a 11x17 poster to attract potential applicants/crew
I have attached a poster that one of our staff made that has all if the relevant info - but i know the poster can look much better than that. I have also attached many images and our logo. It is not necessary to use all of the images, or any of them. The two images of the theater interiors are the venues we operate so they would be the first to include. I can send additional info or images upon request. Thank you

Entertainment

• APPLY@BSCCREWHUB.LA

```html
<!DOCTYPE html>
<html lang="en">
<head>
<meta charset="utf-8">
<title>Brightline Stagecraft Company – Open Positions</title>
<link rel="stylesheet" href="https://fonts.googleapis.com/css2?family=Anton&family=Montserrat:wght@800;900&family=Poppins:wght@300;400;600;700&family=Yellowtail&display=swap">
<style>
  :root {
    --paper: #ffffff;
    --ink: #1d1d1d;
    --brand-blue: #1452c8;
    --bright-blue: #1a5cff;
    --steel: #9a9ca3;
    --night: #17191f;
    --night-blue: #12285e;
    --pale: #d3d9e8;
  }
  * { margin: 0; padding: 0; box-sizing: border-box; }
  html, body { width: 800px; height: 1200px; overflow: hidden; background: var(--paper); }
  .poster {
    position: relative; width: 800px; height: 1200px; overflow: hidden;
    background: var(--paper); font-family: "Poppins", sans-serif;
  }
  .abs { position: absolute; }

  .crew-scene {
    left: 0; top: 0; width: 800px; height: 1200px;
    background: linear-gradient(160deg, #1d3f8a 0%, #142a5c 35%, #1a1d26 75%, var(--night) 100%);
    clip-path: polygon(0 830px, 0 695px, 120px 690px, 300px 660px, 520px 610px, 800px 560px, 800px 1200px, 0 1200px);
  }

  .megaphone { background: radial-gradient(circle at 60% 45%, #f2f3f6 0%, #cfd3dc 55%, #3f63e0 100%); opacity: .95; }
  .megaphone-left { left: 0; top: 63px; width: 245px; height: 357px; border-radius: 0 50% 45% 0 / 0 50% 50% 0; }
  .megaphone-right { left: 632px; top: 333px; width: 168px; height: 204px; border-radius: 50% 0 0 50%; }

  .dot-field { background: var(--pale); opacity: .5; border-radius: 3px; }
  .dots-top { left: 583px; top: 100px; width: 106px; height: 38px; }
  .dots-left { left: 54px; top: 365px; width: 40px; height: 104px; }

  .brand-name {
    left: 0; width: 800px; top: 128px; text-align: center;
    font-weight: 700; font-size: 19px; letter-spacing: .5px; color: var(--brand-blue);
  }
  .brand-rule { left: 300px; top: 160px; width: 200px; height: 2px; background: var(--brand-blue); }

  .has {
    left: 358px; top: 186px; font-family: "Yellowtail", cursive;
    font-size: 78px; line-height: 1; color: var(--brand-blue);
  }
  .headline {
    font-family: "Anton", sans-serif; color: var(--ink); line-height: 1; text-transform: uppercase;
  }
  .headline-open { left: 0; width: 800px; text-align: center; top: 237px; font-size: 138px; padding-left: 4px; }
  .headline-positions { left: 171px; top: 348px; font-size: 138px; letter-spacing: -1px; }

  .photo { border: 4px solid #f4f4f4; box-shadow: 0 3px 10px rgba(0,0,0,.35); }
  .photo-theater { left: 46px; top: 508px; width: 190px; height: 255px; transform: rotate(-3deg);
    background: linear-gradient(160deg, #e08a2a, #a24e12 55%, #5c2a0a); }
  .photo-skyline { left: 233px; top: 530px; width: 170px; height: 240px; transform: rotate(1deg);
    background: linear-gradient(180deg, #10204a 0%, #1c3370 55%, #d7a24a 85%, #1b1b22 100%); }
  .photo-singer { left: 392px; top: 512px; width: 172px; height: 245px; transform: rotate(-1.5deg);
    background: radial-gradient(circle at 55% 30%, #ffffff 0%, #7f94ff 25%, #1e2a8c 60%, #0b0d1c 100%); }
  .photo-concert { left: 556px; top: 548px; width: 190px; height: 240px; transform: rotate(2deg);
    background: radial-gradient(circle at 50% 40%, #9fd6ff 0%, #2a78e6 40%, #0f2f7a 80%, #0a1430 100%); }

  .chevrons { stroke: var(--steel); fill: none; stroke-width: 2; }
  .chev-top { left: 55px; top: 0; }
  .chev-right { left: 664px; top: 195px; }
  .chev-mid { left: 503px; top: 798px; }
  .chev-mid .chevrons { stroke: #4a5f9a; }

  .lead { left: 78px; top: 775px; font-family: "Yellowtail", cursive; font-size: 56px; color: #fff; line-height: 1; }
  .role { left: 76px; font-family: "Montserrat", sans-serif; font-weight: 900; font-size: 60px; line-height: 1; letter-spacing: -1px; }
  .role-talented { top: 850px; color: #fff; }
  .role-technicians { top: 905px; color: #c4c6ce; }

  .roster { left: 78px; top: 970px; color: #fff; line-height: 1.1; letter-spacing: 3px; font-size: 24px; }
  .roster span { display: block; }
  .roster .light { font-weight: 300; }
  .roster .bold { font-weight: 700; }
  .roster .accent { font-weight: 700; color: var(--bright-blue); }

  .resume-label { left: 78px; top: 1080px; color: #fff; font-size: 13px; letter-spacing: 5px; font-weight: 400; }
  .resume-email { left: 78px; top: 1102px; color: #fff; font-size: 22px; font-weight: 700; }

  .site-pill {
    left: 429px; top: 1096px; width: 371px; height: 43px; background: var(--brand-blue);
    border-radius: 8px 0 0 8px; color: #fff; display: flex; align-items: center;
    padding-left: 22px; font-size: 20px; letter-spacing: 4px;
  }
  .site-pill b { font-weight: 700; }
</style>
</head>
<body>
<main class="poster">
  <div class="abs crew-scene" role="img" aria-label="Dark blue photo of a sound technician with headphones working at a mixing console"></div>

  <div class="abs megaphone megaphone-left" role="img" aria-label="Illustrated blue and white megaphone pointing right"></div>
  <div class="abs megaphone megaphone-right" role="img" aria-label="Illustrated blue and white megaphone pointing left"></div>

  <div class="abs dot-field dots-top" role="img" aria-label="Decorative dot grid"></div>
  <div class="abs dot-field dots-left" role="img" aria-label="Decorative dot grid"></div>

  <svg class="abs chev-top" width="30" height="60" viewBox="0 0 30 60" aria-hidden="true">
    <g class="chevrons"><polyline points="2,2 15,10 28,2"/><polyline points="2,14 15,22 28,14"/><polyline points="2,26 15,34 28,26"/><polyline points="2,38 15,46 28,38"/><polyline points="2,50 15,58 28,50"/></g>
  </svg>
  <svg class="abs chev-right" width="78" height="30" viewBox="0 0 78 30" aria-hidden="true">
    <g class="chevrons"><polyline points="2,2 12,15 2,28"/><polyline points="17,2 27,15 17,28"/><polyline points="32,2 42,15 32,28"/><polyline points="47,2 57,15 47,28"/><polyline points="62,2 72,15 62,28"/></g>
  </svg>

  <div class="abs brand-name">Brightline Stagecraft Company</div>
  <div class="abs brand-rule"></div>

  <div class="abs has">has</div>
  <h1>
    <span class="abs headline headline-open">Open</span>
    <span class="abs headline headline-positions">Positions</span>
  </h1>

  <div class="abs photo photo-theater" role="img" aria-label="Ornate historic theater interior with gold balconies"></div>
  <div class="abs photo photo-skyline" role="img" aria-label="Downtown Los Angeles skyline at night"></div>
  <div class="abs photo photo-singer" role="img" aria-label="Silhouetted singer at a microphone under stage lights"></div>
  <div class="abs photo photo-concert" role="img" aria-label="Concert stage with blue light beams over the crowd"></div>

  <svg class="abs chev-mid" width="30" height="74" viewBox="0 0 30 74" aria-hidden="true">
    <g class="chevrons"><polyline points="2,2 15,10 28,2"/><polyline points="2,16 15,24 28,16"/><polyline points="2,30 15,38 28,30"/><polyline points="2,44 15,52 28,44"/><polyline points="2,58 15,66 28,58"/></g>
  </svg>

  <div class="abs lead">We are looking for</div>
  <div class="abs role role-talented">TALENTED</div>
  <div class="abs role role-technicians">TECNICIANS</div>

  <p class="abs roster">
    <span class="light">TO ADD TO OUR</span>
    <span class="bold">ROSTER OF SKILLED</span>
    <span class="accent">PROFESSIONALS</span>
  </p>

  <div class="abs resume-label">SEND RESUME TO</div>
  <div class="abs resume-email">APPLY@BSCCREWHUB.LA</div>

  <div class="abs site-pill">www.<b>bsccrewhub</b>.la</div>
</main>
</body>
</html>
```